TKA Electricial Contracting Services

Hi guys, after a design for my small electrical company, have logo design files to be incorporated into the layout, the basic concept is electrical contracting services for residential, commercial, industrial & data services, image is clean clear and strong,

Card format is to have a nice clean logo on front,with maybe the Residential – commercial – industrial - data, followed with licensed & insured, followed by contact details on backside of the card.

Target Market(s)

Residential, commercial, industrial sectors.

Industry/Entity Type

Electrical

Contact Information for Business Card

TKA logo,
Residential – commercial – industrial - data
REC: 61372
Email: tka@poralink.net.au
Phone: 0458 203 719

Requirements
Must have
• Clean & strong design.
Nice to have
• If possible, I would like the logo colours inverted so the text is orange and the background is black on the front of the card, then the backside of the card be the reverse colour
Should not have
• No Sparks, lightning bolts,

```html
<!DOCTYPE html>
<html lang="en">
<head>
<meta charset="utf-8">
<title>TKA Electricial Contracting Services – Business Card</title>
<link rel="stylesheet" href="https://fonts.googleapis.com/css2?family=Jura:wght@500;700&display=swap">
<style>
  :root {
    --stage: #3b3431;
    --card: #111111;
    --orange: #ef7d16;
    --logo-grey: #4d4d4d;
    --name-grey: #3e3e3e;
    --tag-grey: #777777;
    --ghost: #1c1c1c;
    --white: #ffffff;
  }
  * { box-sizing: border-box; margin: 0; padding: 0; }
  html, body {
    width: 1200px; height: 716px; overflow: hidden;
    background: var(--stage);
    font-family: "Jura", sans-serif;
  }
  .canvas { position: relative; width: 1200px; height: 716px; }
  .card {
    position: absolute; top: 208px;
    width: 520px; height: 300px;
    background: var(--card);
    overflow: hidden;
    box-shadow: 0 10px 28px rgba(0,0,0,.45);
  }
  .card--front { left: 50px; }
  .card--back { left: 630px; }

  /* Front */
  .brand-name {
    position: absolute; left: 34px; top: 22px;
    font-size: 118px; font-weight: 700; line-height: 1;
    color: var(--logo-grey); letter-spacing: 2px;
  }
  .company-name {
    position: absolute; left: 36px; top: 150px;
    font-size: 27px; font-weight: 700;
    color: var(--name-grey);
  }
  .rule {
    position: absolute; left: 36px; top: 188px;
    width: 340px; height: 1px; background: #2e2e2e;
  }
  .services-line {
    position: absolute; left: 36px; top: 196px;
    font-size: 13px; font-weight: 500; color: var(--tag-grey);
    letter-spacing: .3px;
  }
  .accent-block {
    position: absolute; left: 398px; top: 120px;
    width: 96px; height: 112px; background: var(--orange);
  }

  /* Back */
  .ghost-mark {
    position: absolute; left: -10px; bottom: -38px;
    font-size: 190px; font-weight: 700; line-height: 1;
    color: var(--ghost); letter-spacing: 4px;
  }
  .services-panel {
    position: absolute; left: 34px; top: 56px;
    width: 280px; height: 130px; background: var(--orange);
    padding: 34px 0 0 62px;
    color: var(--white); font-size: 17px; font-weight: 700; line-height: 1.2;
  }
  .contact {
    position: absolute; left: 262px; top: 184px;
    color: var(--white); font-size: 17px; font-weight: 700; line-height: 1.3;
    list-style: none;
  }
  .contact li { display: flex; align-items: center; gap: 6px; }
  .contact .licence { padding-left: 40px; }
  .contact svg { width: 13px; height: 13px; flex: none; }
</style>
</head>
<body>
<main class="canvas">
  <section class="card card--front" aria-label="Card front">
    <div class="brand-name">TKA</div>
    <div class="company-name">Tara Kendall Electrical</div>
    <div class="rule"></div>
    <div class="services-line">Residential - commercial - industrial - data</div>
    <div class="accent-block"></div>
  </section>

  <section class="card card--back" aria-label="Card back">
    <div class="ghost-mark" aria-hidden="true">TKA</div>
    <div class="services-panel">Residential - commercial<br>industrial - data</div>
    <ul class="contact">
      <li class="licence">REC: 61372</li>
      <li>
        <svg viewBox="0 0 13 13" aria-hidden="true"><rect x="0.5" y="2" width="12" height="9" fill="none" stroke="#fff" stroke-width="1.4"/><path d="M1 2.5 L6.5 7 L12 2.5" fill="none" stroke="#fff" stroke-width="1.2"/></svg>
        tka@poralink.net.au
      </li>
      <li>
        <svg viewBox="0 0 13 13" aria-hidden="true"><rect x="0" y="0" width="13" height="13" fill="#fff"/><path d="M3.5 2.5 L5 2.5 L5.8 4.6 L4.8 5.4 Q5.6 7.3 7.6 8.2 L8.4 7.2 L10.5 8 L10.5 9.5 Q6 10 3.5 5 Z" fill="#111"/></svg>
        0458 203 719
      </li>
    </ul>
  </section>
</main>
</body>
</html>
```